Business Cards and Stationary for Calmaris Studio (Massage Therapy)
BC for Massage Therapy Studio
Professional
Corwin Palde
President/CEO
742 Fenwick Rd.
Ste. 7C
Halvery, OR 48213
cpalde@studiocalmaris.example
www.studiocalmaris.example
Logo AI file

```html
<!DOCTYPE html>
<html lang="en">
<head>
<meta charset="utf-8">
<title>Calmaris Studio – Business Card</title>
<link rel="stylesheet" href="https://fonts.googleapis.com/css2?family=Cinzel:wght@400&display=swap">
<style>
  :root {
    --page: #e9e4dc;
    --card-dark: #0b0b0b;
    --card-mid: #1c1c1c;
    --gold: #c9c21f;
    --gold-light: #f1ec8a;
    --gold-deep: #8f8a10;
    --ink-light: #f2f2f2;
    --divider: #6b6b6b;
  }
  * { margin: 0; padding: 0; box-sizing: border-box; }
  html, body { width: 1200px; height: 778px; overflow: hidden; background: var(--page); }
  body { position: relative; font-family: "Cinzel", "Times New Roman", serif; }

  .card {
    position: absolute; left: 60px; top: 64px; width: 1080px; height: 650px;
    border-radius: 44px;
    background: radial-gradient(ellipse at 30% 40%, var(--card-mid) 0%, var(--card-dark) 70%);
    box-shadow: 0 6px 18px rgba(0,0,0,0.25);
  }
  .edge-tab {
    position: absolute; top: 262px; width: 34px; height: 136px;
    background: linear-gradient(90deg, var(--gold-deep), var(--gold-light) 45%, var(--gold) 70%, var(--gold-deep));
  }
  .edge-tab--left { left: 0; border-radius: 0 10px 10px 0; }
  .edge-tab--right { right: 0; border-radius: 10px 0 0 10px; }

  .brand { position: absolute; left: 90px; top: 236px; width: 420px; text-align: center; }
  .brand-dot {
    width: 120px; height: 120px; border-radius: 50%; margin: 0 auto 26px;
    background: var(--gold);
  }
  .brand-name {
    font-size: 34px; font-weight: 400; color: var(--ink-light); line-height: 1;
  }

  .divider { position: absolute; left: 536px; top: 160px; width: 1px; height: 340px; background: var(--divider); }

  .contact { position: absolute; left: 572px; top: 202px; color: var(--ink-light); }
  .person-name { font-size: 30px; font-weight: 400; color: var(--gold); line-height: 1.1; }
  .person-title { font-size: 21px; color: var(--gold); margin-top: 4px; }
  .address { font-size: 20px; line-height: 1.3; margin-top: 56px; }
  .lines { list-style: none; margin-top: 6px; font-size: 20px; line-height: 1.32; }
  .lines li { display: flex; align-items: center; gap: 9px; }
  .lines svg { width: 14px; height: 14px; flex: none; }
</style>
</head>
<body>
  <div class="card">
    <div class="edge-tab edge-tab--left"></div>
    <div class="edge-tab edge-tab--right"></div>

    <div class="brand">
      <div class="brand-dot"></div>
      <div class="brand-name">Calmaris Studio</div>
    </div>

    <div class="divider"></div>

    <div class="contact">
      <div class="person-name">Corwin Palde</div>
      <div class="person-title">President/CEO</div>
      <div class="address">742 Fenwick Rd., Ste. 7C<br>Halvery, OR 48213</div>
      <ul class="lines">
        <li>
          <svg viewBox="0 0 14 14" aria-hidden="true"><path d="M3 1l3 3-1.6 1.6a8 8 0 0 0 4 4L10 8l3 3-2 2C6 13 1 8 1 3z" fill="var(--gold)"/></svg>
          555.284.0172
        </li>
        <li>
          <svg viewBox="0 0 14 14" aria-hidden="true"><rect x="1" y="3" width="12" height="8" fill="var(--gold)"/><path d="M1 3l6 5 6-5" stroke="var(--card-dark)" stroke-width="1.2" fill="none"/></svg>
          cpalde@studiocalmaris.example
        </li>
        <li>
          <svg viewBox="0 0 14 14" aria-hidden="true"><circle cx="7" cy="7" r="6" fill="var(--gold)"/><path d="M1 7h12M7 1c-3 3-3 9 0 12M7 1c3 3 3 9 0 12" stroke="var(--card-dark)" stroke-width="1" fill="none"/></svg>
          www.studiocalmaris.example
        </li>
      </ul>
    </div>
  </div>
</body>
</html>
```